European Indian Investment firm

I would like to have a complete make-over of an existing website. Have a look at : www.velmoranpartners-example.com
We are a European/Indian based investment firm that acquires stakes in European (Manufacturing) companies (industrial) and help them grow in India. We have a team in Europe (Barcelona, Zurich, Amsterdam) and in India (Bangalore).
Amongst the new lay-out of the website also the name and the logo of the site will change. I will upload the new company logo. The new site should broadly send out the same message which is bridging Europe and India and also it should have an industrial/manufacturing look. The wording and the various pages of the website will be broadly the same as the old one with some changes which we will provide further down the road. I

Target Market(s)

Europe and India. Entrepreneurs, CEO's and investors.

Industry/Entity Type

Investment

Coding

Coded - Design and coding required

Number of Pages Required

5+ page

Font styles to use
Sans Serif

Requirements
Must have
• site should have an industrial look and also it should reflect the bridging between the two continents Europe and India provided by the team helping companies to grow.

```html
<!DOCTYPE html>
<html lang="en">
<head>
<meta charset="utf-8">
<title>Velmoran Partners – Building truly global European industrial SMEs</title>
<link href="https://fonts.googleapis.com/css2?family=Open+Sans:wght@400;600;700&display=swap" rel="stylesheet">
<style>
:root{
  --teal:#1d4a55;
  --teal-dark:#153840;
  --teal-deep:#0f2b31;
  --accent:#e07b2a;
  --red:#c8332b;
  --ink:#3a3f44;
  --muted:#7a8288;
  --line:#dcdfe2;
  --soft:#f2f3f4;
  --white:#ffffff;
}
*{box-sizing:border-box;margin:0;padding:0}
html,body{width:1200px;height:2288px;overflow:hidden}
body{font-family:"Open Sans",Arial,sans-serif;color:var(--ink);background:var(--white);position:relative;font-size:13px;line-height:1.6}
.site-header{height:84px;position:relative}
.brand{position:absolute;left:40px;top:10px;display:flex;align-items:center;gap:10px}
.brand-mark{width:52px;height:52px;border:2px solid var(--teal);border-radius:50%}
.brand-name{font-weight:700;font-size:18px;color:var(--teal);line-height:1.1}
.top-contact{position:absolute;right:40px;top:22px;display:flex;align-items:center;gap:18px;font-size:12px;color:var(--muted)}
.top-contact span{display:flex;align-items:center;gap:6px}
.social{width:20px;height:20px;background:var(--teal);border-radius:2px;display:inline-block}
.main-nav{position:absolute;top:84px;left:0;width:1200px;height:32px;background:rgba(20,50,58,.92);z-index:2;display:flex;padding-left:150px}
.main-nav a{color:var(--white);text-decoration:none;font-size:11px;font-weight:600;letter-spacing:.06em;padding:0 28px;line-height:32px}
.main-nav a.active{background:var(--accent)}
.hero{position:absolute;top:84px;left:0;width:1200px;height:436px}
.hero-photo{position:absolute;inset:0;background:linear-gradient(110deg,#5a6166 0%,#8b9196 45%,#c9cdd0 70%,#6d7378 100%)}
.hero-content{position:absolute;left:150px;top:110px;width:560px;color:var(--white)}
.hero h1{font-size:34px;font-weight:600;line-height:1.2}
.hero .tag{display:inline-block;background:var(--accent);font-size:12px;font-weight:600;padding:2px 10px;margin-top:10px}
.hero p{font-size:12px;margin-top:12px;line-height:1.5}
.btn{display:inline-block;background:var(--red);color:var(--white);font-size:10px;font-weight:700;letter-spacing:.05em;padding:7px 14px;margin-top:20px}
.intro{position:absolute;top:520px;left:0;width:1200px;height:340px;border-bottom:1px solid var(--line)}
.intro p{position:absolute;left:160px;top:150px;width:640px;font-size:12.5px;color:var(--ink)}
.intro-visual{position:absolute;left:840px;top:40px;width:170px;height:150px;background:radial-gradient(circle at 40% 45%,#1d4a55 0 30%,#5d7e86 55%,transparent 72%),radial-gradient(circle at 75% 70%,#c8332b 0 22%,transparent 45%);border-radius:8px}
.services{position:absolute;top:860px;left:0;width:1200px;height:500px;background:var(--soft)}
.section-title{text-align:center;font-size:22px;font-weight:400;color:var(--ink)}
.services .section-title{margin-top:36px}
.section-sub{text-align:center;font-size:12px;color:var(--muted);margin-top:2px}
.service-grid{position:absolute;left:140px;width:920px;display:grid;gap:20px}
.row-a{top:150px;grid-template-columns:repeat(4,1fr)}
.row-b{top:330px;left:280px;width:640px;grid-template-columns:repeat(3,1fr)}
.service{display:flex;gap:10px}
.service-icon{flex:none;width:34px;height:34px;border-radius:50%;background:var(--teal)}
.service h3{font-size:13px;font-weight:600;color:var(--ink);line-height:1.25}
.service ul{list-style:none;margin-top:8px;font-size:10.5px;color:var(--muted);line-height:1.55}
.service li::before{content:"› ";color:var(--accent)}
.portfolio{position:absolute;top:1360px;left:0;width:1200px;height:520px}
.portfolio .section-title{margin-top:28px}
.portfolio-grid{position:absolute;left:248px;top:68px;width:704px;display:grid;grid-template-columns:repeat(4,1fr);grid-template-rows:208px 208px;gap:12px}
.tile{position:relative}
.tile-text{background:#8f9aa0;color:var(--white);display:flex;align-items:center;justify-content:center;font-size:18px}
.cta{position:absolute;top:1880px;left:0;width:1200px;height:160px;background:var(--teal);text-align:center;color:var(--white)}
.cta h2{font-size:24px;font-weight:600;margin-top:28px}
.cta p{font-size:12px;opacity:.85}
.cta .btn{background:var(--accent);margin-top:14px}
.site-footer{position:absolute;top:2040px;left:0;width:1200px;height:248px;background:var(--teal-dark);color:#c9d4d7}
.footer-cols{position:absolute;left:140px;top:26px;width:920px;display:grid;grid-template-columns:repeat(4,1fr);gap:30px}
.footer-cols h4{color:var(--white);font-size:14px;font-weight:600;margin-bottom:10px}
.footer-cols ul{list-style:none;font-size:11px;line-height:1.9}
.contact-line{display:flex;gap:8px;font-size:11px;margin-bottom:8px;align-items:flex-start}
.news-input{height:26px;background:var(--white);margin:10px 0 8px}
.news-btn{display:inline-block;background:var(--teal);border:1px solid #4d7681;color:var(--white);font-size:10px;padding:3px 10px}
.footer-bar{position:absolute;bottom:0;left:0;width:1200px;height:34px;background:var(--teal-deep);font-size:10px;padding:10px 140px;display:flex;justify-content:space-between}
.footer-bar .socials{display:flex;gap:6px}
</style>
</head>
<body>
<header class="site-header">
  <div class="brand"><span class="brand-mark"></span><span class="brand-name">Velmoran<br>Partners</span></div>
  <div class="top-contact">
    <span><svg width="12" height="12" viewBox="0 0 24 24"><path fill="#7a8288" d="M6.6 10.8a15 15 0 006.6 6.6l2.2-2.2c.3-.3.7-.4 1-.2 1.1.4 2.3.6 3.6.6.6 0 1 .4 1 1V20c0 .6-.4 1-1 1A17 17 0 013 4c0-.6.4-1 1-1h3.5c.6 0 1 .4 1 1 0 1.3.2 2.5.6 3.6.1.3 0 .7-.2 1z"/></svg>+31 20 555 0142</span>
    <span><svg width="12" height="12" viewBox="0 0 24 24"><rect x="2" y="5" width="20" height="14" fill="none" stroke="#7a8288" stroke-width="2"/><path d="M2 5l10 8 10-8" fill="none" stroke="#7a8288" stroke-width="2"/></svg>www.velmoranpartners-example.com</span>
    <span><i class="social"></i><i class="social"></i></span>
  </div>
</header>

<nav class="main-nav">
  <a class="active">ORIGINATION</a><a>STRATEGY</a><a>TEAM</a><a>PORTFOLIO</a><a>PUBLICATIONS</a><a>INVESTORS</a><a>CONTACT</a>
</nav>

<section class="hero">
  <div class="hero-photo" role="img" aria-label="Grey-toned industrial machinery photo overlaid with engineering sketch lines"></div>
  <div class="hero-content">
    <h1>Building truly global European industrial SMEs</h1>
    <span class="tag">Bridging Europe and India</span>
    <p>We are a European/Indian based investment firm that acquires stakes in European manufacturing companies and helps them grow in India.</p>
    <span class="btn">HOW TO GET STARTED GUIDE</span>
  </div>
</section>

<section class="intro">
  <div class="intro-visual" role="img" aria-label="Illustration of interlocking teal and red gears"></div>
  <p>Velmoran Partners is a Euro-Indian partnership that invests in European industrial SMEs that face a growth challenge. We acquire controlling stakes in businesses having "special situations": either underperformance, shareholder issues, distress or tight cash positions. Our target companies are basic processing and manufacturing industries, a segment of industry that is steadily losing base in declining home markets. We also team up with European industrial groups to set up stand-alone Joint Ventures to develop the Indian market.</p>
</section>

<section class="services">
  <h2 class="section-title">Our Services</h2>
  <p class="section-sub">Our target companies are operating in the ELT "discontinuities"</p>
  <div class="service-grid row-a">
    <div class="service"><span class="service-icon"></span><div><h3>Infrastructure &amp; Construction</h3><ul><li>Structural materials</li><li>Infrastructure design</li><li>Building systems</li><li>Outdoor products</li></ul></div></div>
    <div class="service"><span class="service-icon"></span><div><h3>Automotive &amp; transport</h3><ul><li>Systems (tier 1)</li><li>Components (tier 2)</li><li>Transport vehicles</li><li>Aftermarket</li></ul></div></div>
    <div class="service"><span class="service-icon"></span><div><h3>Engineered products</h3><ul><li>Industrial machinery</li><li>Electrical products</li><li>Engineering</li></ul></div></div>
    <div class="service"><span class="service-icon"></span><div><h3>Consumer goods &amp; retail</h3><ul><li>Food &amp; beverages</li><li>Processed food</li><li>Apparel, footwear &amp; accessories</li><li>Furniture &amp; furnishing</li><li>Appliances</li></ul></div></div>
  </div>
  <div class="service-grid row-b">
    <div class="service"><span class="service-icon"></span><div><h3>Basic process industries</h3><ul><li>Steel</li><li>Petrochemicals</li><li>Pulp &amp; paper</li><li>Glass</li><li>Leather &amp; textile</li></ul></div></div>
    <div class="service"><span class="service-icon"></span><div><h3>Advanced materials</h3><ul><li>Textiles &amp; fabrics</li><li>Specialty metals</li><li>Paints &amp; coatings</li><li>Specialty chemicals</li><li>Special materials</li></ul></div></div>
    <div class="service"><span class="service-icon"></span><div><h3>Healthcare</h3><ul><li>Diagnostic solutions</li><li>Treatment solutions</li><li>Specialty materials</li><li>Specialty equipment</li></ul></div></div>
  </div>
</section>

<section class="portfolio">
  <h2 class="section-title">Our Portfolio</h2>
  <div class="portfolio-grid">
    <div class="tile" role="img" aria-label="Industrial robot arm in a factory" style="background:linear-gradient(135deg,#6f8ea0,#c7d3da)"></div>
    <div class="tile" role="img" aria-label="Close-up of metal gears" style="background:linear-gradient(135deg,#4d4e50,#9a9c9e)"></div>
    <div class="tile" role="img" aria-label="Glass structure with green plants" style="background:linear-gradient(135deg,#4d7a3e,#a9c98c)"></div>
    <div class="tile" role="img" aria-label="Factory production hall" style="background:linear-gradient(135deg,#8c8c8c,#d8d8d8)"></div>
    <div class="tile tile-text">Lorem ipsum dolor</div>
    <div class="tile" role="img" aria-label="Welding sparks in a workshop" style="background:radial-gradient(circle at 50% 40%,#e9eef5,#4a6a8e 70%)"></div>
    <div class="tile" role="img" aria-label="Modern building facade" style="background:linear-gradient(135deg,#b08a62,#e6d3bb)"></div>
    <div class="tile" role="img" aria-label="Industrial machinery interior" style="background:linear-gradient(135deg,#5c6670,#a8b0b6)"></div>
  </div>
</section>

<section class="cta">
  <h2>How do I get started?</h2>
  <p>Click button below to Request a Quote. I will have a document on my letterhead with required information.</p>
  <span class="btn">How to get started guide</span>
</section>

<footer class="site-footer">
  <div class="footer-cols">
    <div><h4>Main menu</h4><ul><li>Home</li><li>Strategy</li><li>Portfolio</li><li>Investors</li><li>Contact us</li></ul></div>
    <div><h4>Information</h4><ul><li>Advisory</li><li>Legal Notice</li><li>Terms and conditions of use</li><li>Privacy statement</li><li>Site map</li></ul></div>
    <div><h4>Contact us</h4>
      <div class="contact-line"><svg width="12" height="14" viewBox="0 0 24 28"><path fill="#c9d4d7" d="M12 0a10 10 0 00-10 10c0 8 10 18 10 18s10-10 10-18A10 10 0 0012 0zm0 14a4 4 0 110-8 4 4 0 010 8z"/></svg><span>12 Harbour Street 45 suite<br>Amsterdam, 1000</span></div>
      <div class="contact-line"><svg width="12" height="12" viewBox="0 0 24 24"><path fill="#c9d4d7" d="M6.6 10.8a15 15 0 006.6 6.6l2.2-2.2c.3-.3.7-.4 1-.2 1.1.4 2.3.6 3.6.6.6 0 1 .4 1 1V20c0 .6-.4 1-1 1A17 17 0 013 4c0-.6.4-1 1-1h3.5c.6 0 1 .4 1 1 0 1.3.2 2.5.6 3.6.1.3 0 .7-.2 1z"/></svg><span>+31 20 555 0142</span></div>
      <div class="contact-line"><svg width="12" height="12" viewBox="0 0 24 24"><rect x="2" y="5" width="20" height="14" fill="none" stroke="#c9d4d7" stroke-width="2"/><path d="M2 5l10 8 10-8" fill="none" stroke="#c9d4d7" stroke-width="2"/></svg><span>info@velmoranpartners-example.com</span></div>
    </div>
    <div><h4>Newsletter</h4><p style="font-size:11px">Receive our latest news</p><div class="news-input"></div><span class="news-btn">Submit</span></div>
  </div>
  <div class="footer-bar"><span>© 2015 Velmoran Partners B.V. All rights reserved</span><span class="socials"><i class="social" style="background:#3d6b77"></i><i class="social" style="background:#3d6b77"></i></span></div>
</footer>
</body>
</html>
```